Brambleford Homepage Design

We need a home page design for Brambleford. Brambleford creates gear for outdoor enthusiasts who are passionate about conservation, wildlife observation, and ethical hunting.

Current Website: www.bramblekit.example

Customer Avatar Canvas:
https://sheets.example.net/d/9XqLmRtVwYzAbCdEfGhJkNpQrStUvWxYz12345678/edit#gid=10293847

Homepage Template: Attached below
https://files.example.net/folders/7k3HsPqWmZtRvBnLcXyDfGjQaUeTo

There is info on imagery in the homepage template. Where there isn't, appropriate stock imagery is acceptable.

Logo Design and Product Images: https://files.example.net/folders/4mNbVcXzLkJhGfDsAqWeRtYuIoPzZ

```html
<!DOCTYPE html>
<html lang="en">
<head>
<meta charset="utf-8">
<title>Brambleford — Home</title>
<link rel="stylesheet" href="https://fonts.googleapis.com/css2?family=Poppins:wght@300;400;500;600;700&display=swap">
<style>
:root{
  --ink:#2b2b2b;
  --ink-soft:#555;
  --dark:#2d2d2d;
  --dark-alt:#3a3a3a;
  --bar:#454545;
  --card:#f1f1f1;
  --light:#f5f5f5;
  --white:#fff;
  --mark-grey:#9a9a9a;
  --badge-shadow:#8d8d8d;
}
*{box-sizing:border-box;margin:0;padding:0}
html,body{width:1200px;height:4584px;overflow:hidden}
body{font-family:"Poppins",sans-serif;color:var(--ink);background:var(--white);position:relative}

/* header */
.site-header{position:absolute;left:0;top:0;width:1200px;height:128px;background:var(--white)}
.brand{position:absolute;font-family:"Poppins",sans-serif;font-weight:700;letter-spacing:1px;white-space:nowrap}
.site-header .brand{left:86px;top:46px;font-size:26px;color:var(--ink)}
.main-nav{position:absolute;top:60px;font-size:15px;color:var(--ink-soft)}
.shop-btn{position:absolute;left:968px;top:44px;width:146px;height:52px;border-radius:26px;background:var(--ink);color:var(--white);font-size:13px;font-weight:500;display:flex;align-items:center;justify-content:center}

/* hero */
.hero{position:absolute;left:0;top:128px;width:1200px;height:639px;background:linear-gradient(160deg,#6f7568 0%,#4f5a45 35%,#3f4d30 60%,#56612f 100%)}
.hero-line{position:absolute;left:87px;color:var(--white);font-size:31px;font-weight:300;line-height:41px}
.hero-btn{position:absolute;top:388px;height:86px;border-radius:18px;font-size:15px;line-height:19px;display:flex;align-items:center;justify-content:center;text-align:center}
.hero-btn.light{left:87px;width:251px;background:var(--white);color:var(--ink)}
.hero-btn.ghost{left:360px;width:281px;background:var(--dark);color:var(--white);border:2px solid var(--white)}
.dots{position:absolute;left:562px;top:568px;display:flex;gap:4px}
.dots span{width:15px;height:15px;border-radius:50%;background:#9a9a9a}
.dots span:first-child{background:var(--white)}

/* partner band */
.partners{position:absolute;left:0;top:767px;width:1200px;height:289px;background:var(--white)}
.partners .brand{font-size:18px;color:var(--mark-grey);top:132px;width:160px;margin-left:-80px;text-align:center}

/* video */
.video-section{position:absolute;left:0;top:1056px;width:1200px;height:739px;background:var(--dark)}
.video-frame{position:absolute;left:87px;top:87px;width:1029px;height:422px;background:linear-gradient(135deg,#3a352d,#6b6152 45%,#8a7a62 60%,#2f2b25)}
.play{position:absolute;left:460px;top:158px}
.video-btn{position:absolute;left:313px;top:561px;width:574px;height:96px;border-radius:20px;background:var(--white);color:var(--ink);font-size:21px;display:flex;align-items:center;justify-content:center}

/* how it works */
.how{position:absolute;left:0;top:1795px;width:1200px;height:1091px;background:var(--white)}
.section-title{position:absolute;left:0;width:1200px;text-align:center;font-weight:600;font-size:41px}
.how-sub{position:absolute;left:0;top:194px;width:1200px;text-align:center;font-size:20px;color:#444}
.step{position:absolute;width:508px}
.step.filled{background:var(--card)}
.badge{position:absolute;left:43px;width:76px;height:66px}
.badge i{position:absolute;left:10px;top:10px;width:76px;height:66px;border-radius:12px;background:var(--badge-shadow)}
.badge b{position:absolute;left:0;top:0;width:76px;height:66px;border-radius:12px;background:var(--ink);color:var(--white);font-size:19px;font-weight:600;line-height:22px;display:flex;align-items:center;justify-content:center;text-align:center}
.step h3{position:absolute;left:23px;right:23px;font-size:16px;font-weight:600;line-height:20px}
.step p{position:absolute;left:23px;right:23px;font-size:14.5px;line-height:25.8px;color:#5a5a5a;font-weight:300}

/* who it's for */
.who{position:absolute;left:0;top:2886px;width:1200px;height:860px;background:var(--dark-alt)}
.who .section-title{color:var(--white);top:128px}
.who-box{position:absolute;padding:58px 37px 0;font-size:15px;line-height:26px;text-align:justify;font-weight:300}
.who-box.white{background:var(--white);color:var(--ink)}
.who-box.outline{border:1px solid #cfcfcf;color:var(--white);background:var(--dark-alt)}

/* cta */
.cta{position:absolute;left:0;top:3746px;width:1200px;height:447px;background:var(--light)}
.cta .section-title{top:102px;font-size:39px;line-height:48px;font-weight:600}
.cta-btn{position:absolute;left:290px;top:239px;width:630px;height:94px;border-radius:10px;background:var(--ink);color:var(--white);font-size:24px;display:flex;align-items:center;justify-content:center}

/* footer */
.site-footer{position:absolute;left:0;top:4193px;width:1200px;height:335px;background:var(--dark)}
.site-footer .brand{left:86px;top:124px;font-size:30px;color:var(--white)}
.foot-head{position:absolute;top:72px;color:var(--white);font-size:19px;font-weight:500}
.foot-links{position:absolute;left:365px;top:130px;list-style:none;color:var(--white);font-size:15px}
.foot-links li{height:41px;padding-left:24px;position:relative}
.foot-links li:before{content:"";position:absolute;left:2px;top:8px;width:7px;height:7px;border-radius:50%;background:var(--white)}
.contact{position:absolute;left:607px;width:250px;color:var(--white);font-size:17px;display:flex;align-items:flex-start;gap:14px;line-height:19px;white-space:nowrap}
.contact svg{flex:none;margin-top:1px}
.social{position:absolute;display:flex;align-items:center;gap:14px;color:var(--white);font-size:10px;white-space:nowrap}
.social span.dot{width:29px;height:29px;border-radius:50%;background:#5a5a5a}
.copyright{position:absolute;left:0;top:4528px;width:1200px;height:56px;background:var(--bar);color:var(--white);font-size:14px}
.copyright .l{position:absolute;left:87px;top:18px}
.copyright .r{position:absolute;right:87px;top:18px}
</style>
</head>
<body>

<header class="site-header">
  <div class="brand">BRAMBLEFORD</div>
  <nav>
    <span class="main-nav" style="left:689px">Features</span>
    <span class="main-nav" style="left:792px">About Us</span>
    <span class="main-nav" style="left:899px">Log In</span>
  </nav>
  <div class="shop-btn">SHOP GEAR</div>
</header>

<section class="hero" role="img" aria-label="Hunter with binoculars on a mountain trail above a forested valley">
  <div class="hero-line" style="top:114px">“Explore the Wild West: Embrace Conservation,<br>Hunt Ethically, and Protect Public Lands with Brambleford Gear"</div>
  <div class="hero-line" style="top:230px">"Elevate Your Outdoor Adventures<br>While Supporting Conservation Efforts"</div>
  <div class="hero-btn light">Order Your Brambleford<br>Bino Harness Today!</div>
  <div class="hero-btn ghost">Unlock the Power of Optics<br>and Preserve the Wild</div>
  <div class="dots"><span></span><span></span><span></span><span></span></div>
</section>

<section class="partners">
  <div class="brand" style="left:207px">BRAMBLEFORD</div>
  <div class="brand" style="left:402px">BRAMBLEFORD</div>
  <div class="brand" style="left:606px">BRAMBLEFORD</div>
  <div class="brand" style="left:800px">BRAMBLEFORD</div>
  <div class="brand" style="left:990px">BRAMBLEFORD</div>
</section>

<section class="video-section">
  <div class="video-frame" role="img" aria-label="Bull elk walking through a dark forest">
    <svg class="play" width="106" height="106" viewBox="0 0 106 106"><circle cx="53" cy="53" r="53" fill="#fff"/><path d="M42 33 L74 53 L42 73 Z" fill="#2b2b2b"/></svg>
  </div>
  <div class="video-btn">Order Your Brambleford Bino Harness Today!</div>
</section>

<section class="how">
  <h2 class="section-title" style="top:112px">How It Works</h2>
  <p class="how-sub">Introducing the Brambleford Bino Harness – The Ultimate Companion for Your Optics</p>

  <div class="step filled" style="left:87px;top:277px;height:335px">
    <div class="badge" style="top:29px"><i></i><b>STEP<br>01</b></div>
    <h3 style="top:123px">Experience unparalleled convenience and comfort during your outdoor excursions with the Brambleford Bino Harness</h3>
    <p style="top:192px">Designed specifically for the modern conservationist and avid hunter, this innovative harness combines functionality, durability, and style to enhance your wildlife observation and hunting experiences.</p>
  </div>

  <div class="step" style="left:607px;top:277px;height:335px">
    <div class="badge" style="top:29px"><i></i><b>STEP<br>02</b></div>
    <h3 style="top:123px">Unmatched Optics Protection:</h3>
    <p style="top:158px">Our Bino Harness features a secure and adjustable harness system that keeps your binoculars safe and within easy each at all times. No more fumbling around or worrying about accidentally dropping your expensive optics. With the Brambleford Bino Harness, your binoculars are securely trapped to your chest, offering quick and hassle-free access whenever you need them.</p>
  </div>

  <div class="step" style="left:87px;top:655px;height:349px">
    <div class="badge" style="top:29px"><i></i><b>STEP<br>03</b></div>
    <h3 style="top:123px">Thoughtful Design for Easy Access:</h3>
    <p style="top:158px">We've incorporated thoughtful design elements into the Brambleford Bino Harness to enhance your outdoor adventures. The quick-release buckles allow for swift and effortless removal of the harness, granting you unhindered mobility when necessary. The adjustable straps ensure a personalized fit for individuals of all body types.</p>
  </div>

  <div class="step filled" style="left:607px;top:655px;height:349px">
    <div class="badge" style="top:29px"><i></i><b>STEP<br>04</b></div>
    <h3 style="top:123px">Embrace Conservation:</h3>
    <p style="top:158px">By choosing the Brambleford Bino Harness, you're not only investing in a premium gear accessory but also supporting the conservation of public lands and wildlife. We are dedicated to promoting sustainable hunting and ethical practices, and a portion of the proceeds from every purchase goes towards initiatives that preserve the habitats we hold dear.</p>
  </div>
</section>

<section class="who">
  <h2 class="section-title">Who It’s For</h2>
  <div class="who-box white" style="left:87px;top:247px;width:508px;height:333px">The Brambleford Bino Harness is the ideal gear accessory for outdoor enthusiasts who are passionate about conservation, wildlife observation, and ethical hunting. This product is designed for individuals who value the preservation of public lands, appreciate the beauty of the American West, and seek to engage in sustainable and responsible outdoor pursuits.</div>
  <div class="who-box outline" style="left:607px;top:247px;width:509px;height:333px">Additionally, the Brambleford Bino Harness appeals to those who prioritize durability and reliability in their gear. Whether you're exploring rugged terrains, participating in long hikes, or embarking on extended hunting trips, this harness will securely hold your binoculars, providing peace of mind and allowing you to focus on the beauty of nature.</div>
  <div class="who-box outline" style="left:150px;top:514px;width:466px;height:237px;padding-top:38px;padding-left:22px;padding-right:32px">This harness is perfect for avid hunters who want quick and easy access to their binoculars without compromising on comfort. It is also ideal for wildlife photographers, birdwatchers, and nature enthusiasts who rely on high-quality optics to capture stunning images or observe wildlife in their natural habitats.</div>
  <div class="who-box white" style="left:669px;top:514px;width:467px;height:237px;padding-top:38px;padding-left:24px;padding-right:20px">The Brambleford Bino Harness is designed for outdoor enthusiasts who embrace a conservation-centered lifestyle, value ethical hunting practices, and appreciate the unique opportunities offered by the American West.</div>
</section>

<section class="cta">
  <h2 class="section-title">Unlock the Power of Optics and<br>Preserve the Wild</h2>
  <div class="cta-btn">Order Your Brambleford Bino Harness Today!</div>
</section>

<footer class="site-footer">
  <div class="brand">BRAMBLEFORD</div>

  <div class="foot-head" style="left:365px">QUIK LINKS</div>
  <ul class="foot-links"><li>Feautures</li><li>About Us</li><li>Log In</li></ul>

  <div class="foot-head" style="left:607px">CONTACT US</div>
  <div class="contact" style="top:135px">
    <svg width="20" height="20" viewBox="0 0 20 20"><rect width="20" height="20" rx="4" fill="#fff"/><path d="M6 5c1 0 1.5 2 2 3l-1 1c.7 1.5 2 2.8 3.5 3.5l1-1c1 .5 3 1 3 2 0 1-1 2-2 2C8 15 5 12 4.5 7c0-1 .5-2 1.5-2z" fill="#2d2d2d"/></svg>
    <span>+012 555 0142</span></div>
  <div class="contact" style="top:186px">
    <svg width="20" height="20" viewBox="0 0 20 20"><rect width="20" height="20" rx="4" fill="#fff"/><rect x="4.5" y="6" width="11" height="8" fill="none" stroke="#2d2d2d" stroke-width="1.5"/><path d="M4.5 6l5.5 4.5L15.5 6" fill="none" stroke="#2d2d2d" stroke-width="1.5"/></svg>
    <span>hi@brambleford.example</span></div>
  <div class="contact" style="top:239px">
    <svg width="20" height="20" viewBox="0 0 20 20"><rect width="20" height="20" rx="4" fill="#fff"/><path d="M10 4a4 4 0 0 1 4 4c0 3-4 8-4 8s-4-5-4-8a4 4 0 0 1 4-4z" fill="#2d2d2d"/><circle cx="10" cy="8" r="1.5" fill="#fff"/></svg>
    <span style="font-size:15px">Address line Dummy Here<br>Address line Here</span></div>

  <div class="foot-head" style="left:874px">FOLLOW US</div>
  <div class="social" style="left:874px;top:136px"><span class="dot"></span>Campfire</div>
  <div class="social" style="left:1017px;top:136px"><span class="dot"></span>TrailCast</div>
  <div class="social" style="left:874px;top:177px"><span class="dot"></span>Snapline</div>
  <div class="social" style="left:1017px;top:177px"><span class="dot"></span>Workbench</div>
  <div class="social" style="left:874px;top:218px"><span class="dot"></span>Chirper</div>
</footer>

<div class="copyright">
  <span class="l">Copyright © 2023 All Rights Reserved By Brambleford</span>
  <span class="r">Terms of Service | Privacy Policy</span>
</div>

</body>
</html>
```